Cover for a pop up stand relating to bespoke gins

We need a design for a pop up counter that tells people what we do in a clear message.
We will be using the pop up counter in an exhibition and want to attract bar owners to come to talk to us about us making them a bottle of branded gin for their bar. I will be standing behind the counter and people passing should take an interest in the graphic on the front of the counter and come and talk to be about what we do.
We make high quality gin for bars and we brand the gin with their logo. The gin is bespoke and made to their specification. No two bars get the same gin and the label on the bottle of gin uses the brand of the bar.
The message needs to be very short and clear and just enough to attract somebody walking past in an exhibition. The message about how the process works is not needed - just the headline "Would you like your own Gin Brand?".
Target Market(s)
People who own upmarket bars who are attending an event to find new products to sell in their bar.
Requirements
Must have
- Must project the clear message that
- "Would you like your own Gin Brand?"
- So, for example, the owner of a bar called The Gold Hare could have a gin that is called Gold Hare Gin with The Gold Hare logo.
Nice to have
- It could show some of the gin bottles they we already make for other pubs.
- The large poster we have behind us is Pink and advertises Blue Owl Gin so use of Pink in the design is a possibility. The surrounding walls and the carpet are black.
Should not have
- simple message more important that graphics or complex descriptions

```html
<!DOCTYPE html>
<html lang="en">
<head>
<meta charset="utf-8">
<title>Create Bespoke Gin For Your Bar – Counter Cover</title>
<link rel="stylesheet" href="https://fonts.googleapis.com/css2?family=Roboto+Condensed:wght@700&display=swap">
<style>
  :root {
    --page: #ffffff;
    --headline-red: #e5231d;
    --outline-white: #ffffff;
    --water-deep: #1f8fd6;
    --water-mid: #5cc3f0;
    --water-light: #bfe9fb;
    --glass: rgba(230, 247, 255, 0.55);
    --glass-edge: rgba(255, 255, 255, 0.8);
    --lime: #8cc63f;
    --bottle-clear: #e9eef0;
    --bottle-cap: #d9a441;
  }
  * { box-sizing: border-box; margin: 0; padding: 0; }
  html, body {
    width: 1200px; height: 1200px; overflow: hidden;
    background: var(--page);
  }
  .counter-cover {
    position: absolute;
    left: 37px; top: 272px;
    width: 1126px; height: 655px;
    overflow: hidden;
    font-family: "Roboto Condensed", "Arial Narrow", sans-serif;
    font-weight: 700;
  }
  .water-backdrop {
    position: absolute; inset: 0;
    background:
      radial-gradient(ellipse at 50% 40%, var(--water-light) 0%, var(--water-mid) 45%, var(--water-deep) 100%);
  }
  .tonic-glass {
    position: absolute; top: 40px; width: 120px; height: 510px;
    border-radius: 6px 6px 18px 18px;
    background: linear-gradient(90deg, var(--glass-edge), var(--glass) 30%, var(--glass) 70%, var(--glass-edge));
  }
  .tonic-glass .lime-wedge {
    position: absolute; top: 225px; left: 8px; width: 100px; height: 100px;
    border-radius: 50%; background: radial-gradient(circle, #d7ef8a, var(--lime));
  }
  .tonic-glass--left { left: 293px; }
  .tonic-glass--right { left: 743px; }
  .hero-bottle {
    position: absolute; left: 408px; top: 0; width: 335px; height: 600px;
    border-radius: 150px 150px 40px 40px;
    background: linear-gradient(180deg, rgba(255,255,255,0.75) 0%, rgba(210,240,255,0.7) 60%, rgba(120,200,240,0.8) 100%);
  }
  .headline {
    position: absolute;
    text-align: center;
    color: var(--headline-red);
    text-transform: uppercase;
    letter-spacing: -0.5px;
    text-shadow:
      3px 0 0 var(--outline-white), -3px 0 0 var(--outline-white),
      0 3px 0 var(--outline-white), 0 -3px 0 var(--outline-white),
      2px 2px 0 var(--outline-white), -2px -2px 0 var(--outline-white),
      2px -2px 0 var(--outline-white), -2px 2px 0 var(--outline-white);
  }
  .headline span { display: block; }
  .headline--side { top: 48px; width: 200px; }
  .headline--side .line { font-size: 48px; line-height: 46px; }
  .headline--side .line--gin { font-size: 72px; line-height: 62px; }
  .headline--side .line--bar { font-size: 66px; line-height: 58px; }
  .headline--left { left: 38px; }
  .headline--right { left: 893px; }
  .headline--centre { left: 408px; top: 122px; width: 335px; }
  .headline--centre .line { font-size: 78px; line-height: 70px; }
  .headline--centre .line--gin { font-size: 116px; line-height: 98px; }
  .headline--centre .line--bar { font-size: 112px; line-height: 96px; }
  .client-bottle {
    position: absolute;
    background: linear-gradient(90deg, #c8d0d4, var(--bottle-clear) 35%, #ffffff 60%, #c8d0d4);
  }
  .client-bottle--marlow {
    left: 91px; top: 335px; width: 94px; height: 245px;
    border-radius: 40px 40px 8px 8px;
  }
  .client-bottle--hollins {
    left: 941px; top: 350px; width: 84px; height: 230px;
    border-radius: 28px 28px 8px 8px;
  }
</style>
</head>
<body>
  <section class="counter-cover">
    <div class="water-backdrop" role="img" aria-label="Photograph of sparkling blue water full of bubbles"></div>

    <div class="tonic-glass tonic-glass--left" role="img" aria-label="Photograph of a tall gin and tonic glass with a lime wedge"><div class="lime-wedge"></div></div>
    <div class="tonic-glass tonic-glass--right" role="img" aria-label="Photograph of a tall gin and tonic glass with a lime wedge"><div class="lime-wedge"></div></div>
    <div class="hero-bottle" role="img" aria-label="Photograph of a large clear gin bottle"></div>

    <h2 class="headline headline--left headline--side">
      <span class="line">Create</span>
      <span class="line">Bespoke</span>
      <span class="line line--gin">Gin</span>
      <span class="line">For Your</span>
      <span class="line line--bar">Bar</span>
    </h2>

    <h1 class="headline headline--centre">
      <span class="line">Create</span>
      <span class="line">Bespoke</span>
      <span class="line line--gin">Gin</span>
      <span class="line">For Your</span>
      <span class="line line--bar">Bar</span>
    </h1>

    <h2 class="headline headline--right headline--side">
      <span class="line">Create</span>
      <span class="line">Bespoke</span>
      <span class="line line--gin">Gin</span>
      <span class="line">For Your</span>
      <span class="line line--bar">Bar</span>
    </h2>

    <div class="client-bottle client-bottle--marlow" role="img" aria-label="Photograph of a Marlow Gin bottle made for a client bar"></div>
    <div class="client-bottle client-bottle--hollins" role="img" aria-label="Photograph of a Hollins Inn Gin bottle made for a client bar"></div>
  </section>
</body>
</html>
```